Resume

I am an industrial designer that has just graduated from school. I have been trying to brand myself when applying to companies. Even though I know of the basic principles in graphic design I have difficulty executing it. I have supplied my logo (which is simple but clean) and two forms of my resume I was playing around with. One is Mostly text the other has more color and is more graphic. I would like something in the middle. I would like to have a creative graph that is easy to read that displays my skills.
Updates

Reason: Some of the designers were asking for an extra day. I gave it 3.

Industry/Entity Type

Graphic Design

```html
<!DOCTYPE html>
<html lang="en">
<head>
<meta charset="utf-8">
<title>Owen Marlowe – Industrial Designer Resume</title>
<link rel="stylesheet" href="https://fonts.googleapis.com/css2?family=Source+Sans+3:wght@300;400;600&display=swap">
<style>
  :root {
    --accent: #b22d26;
    --text: #6f6f6f;
    --text-strong: #5a5a5a;
    --ring-label: #8a8a8a;
    --rule: #a9a9a9;
    --page-border: #8c8c8c;
    --paper: #ffffff;
    --backdrop: #ffffff;
  }
  * { box-sizing: border-box; margin: 0; padding: 0; }
  html, body { width: 1200px; height: 1000px; overflow: hidden; background: var(--backdrop); }
  body { font-family: "Source Sans 3", "Myriad Pro", Arial, sans-serif; color: var(--text); }

  .canvas { position: relative; width: 1200px; height: 1000px; }
  .resume {
    position: absolute; left: 248px; top: 55px; width: 686px; height: 886px;
    background: var(--paper); border: 1px solid var(--page-border);
  }
  .rules { position: absolute; left: 0; top: 0; width: 1200px; height: 1000px; }

  .brand-mark {
    position: absolute; left: 276px; top: 85px; width: 79px; height: 63px;
    border: 3px solid var(--accent); border-radius: 6px;
  }
  .name {
    position: absolute; left: 373px; top: 91px;
    font-size: 36px; line-height: 36px; font-weight: 400; color: var(--accent); letter-spacing: 0.2px;
  }
  .role {
    position: absolute; left: 374px; top: 123px;
    font-size: 16px; line-height: 16px; color: var(--text); letter-spacing: 0.2px;
  }

  .contact-icon { position: absolute; }
  .contact-text {
    position: absolute; width: 200px; text-align: center;
    font-size: 11px; line-height: 13px; top: 250px; color: var(--text);
  }

  .section-title {
    position: absolute; width: 300px; text-align: center;
    font-size: 16px; line-height: 16px; color: var(--accent); font-weight: 400;
  }

  .entry {
    position: absolute; width: 220px; text-align: center;
    font-size: 11px; line-height: 13.6px; color: var(--text);
  }
  .entry strong { font-weight: 600; color: var(--text-strong); }

  .meter { position: absolute; width: 80px; }
  .meter svg { display: block; width: 80px; height: 80px; }
  .meter-value {
    position: absolute; left: 0; top: 0; width: 80px; height: 80px;
    display: flex; align-items: center; justify-content: center;
    font-size: 20px; font-weight: 300; color: var(--ring-label);
  }
  .meter-label {
    position: absolute; left: -30px; top: 80px; width: 140px; text-align: center;
    font-size: 11px; line-height: 12px; color: var(--text); text-transform: uppercase;
  }
  .meter-track { fill: none; stroke: var(--accent); stroke-width: 5.5; }
</style>
</head>
<body>
<div class="canvas">
  <section class="resume" aria-label="Resume"></section>

  <svg class="rules" viewBox="0 0 1200 1000" aria-hidden="true">
    <g stroke="var(--rule)" stroke-width="1">
      <line x1="276" y1="170" x2="907" y2="170"/>
      <line x1="486" y1="180" x2="486" y2="269"/>
      <line x1="697" y1="180" x2="697" y2="269"/>
      <line x1="276" y1="282" x2="907" y2="282"/>
      <line x1="272" y1="455" x2="904" y2="455"/>
      <line x1="272" y1="657" x2="904" y2="657"/>
      <line x1="631" y1="680" x2="631" y2="920"/>
    </g>
    <g class="timeline" stroke="var(--accent)" fill="none">
      <line x1="386" y1="352" x2="790" y2="352" stroke-width="1.6"/>
      <line x1="342" y1="571" x2="834" y2="571" stroke-width="1.6"/>
    </g>
    <g class="timeline-nodes" fill="#fff" stroke="var(--accent)" stroke-width="1.6">
      <circle cx="386" cy="352" r="7.5"/><circle cx="790" cy="352" r="7.5"/>
      <circle cx="342" cy="571" r="7.5"/><circle cx="506" cy="571" r="7.5"/>
      <circle cx="670" cy="571" r="7.5"/><circle cx="834" cy="571" r="7.5"/>
    </g>
    <g fill="var(--accent)">
      <circle cx="386" cy="352" r="4"/><circle cx="790" cy="352" r="4"/>
      <circle cx="342" cy="571" r="4"/><circle cx="506" cy="571" r="4"/>
      <circle cx="670" cy="571" r="4"/><circle cx="834" cy="571" r="4"/>
    </g>
  </svg>

  <header>
    <div class="brand-mark" aria-hidden="true"></div>
    <h1 class="name">OWEN MARLOWE</h1>
    <p class="role">INDUSTRIAL DESIGNER</p>
  </header>

  <!-- Contact -->
  <svg class="contact-icon" style="left:364px;top:190px" width="38" height="52" viewBox="0 0 38 52" aria-label="Phone" role="img">
    <rect x="0" y="0" width="38" height="52" rx="5" fill="var(--accent)"/>
    <rect x="7" y="7" width="24" height="26" fill="#fff"/>
    <circle cx="19" cy="42" r="4" fill="#fff"/>
  </svg>
  <p class="contact-text" style="left:282px">1.555.014.2287</p>

  <svg class="contact-icon" style="left:566px;top:197px" width="52" height="37" viewBox="0 0 52 37" aria-label="Email" role="img">
    <rect x="0" y="0" width="52" height="37" fill="var(--accent)"/>
    <polyline points="0,3 26,22 52,3" fill="none" stroke="#fff" stroke-width="3"/>
  </svg>
  <p class="contact-text" style="left:491px">madebyowen@mailbox.com</p>

  <svg class="contact-icon" style="left:773px;top:186px" width="55" height="57" viewBox="0 0 55 57" aria-label="Website" role="img">
    <polygon points="27.5,0 55,26 48,26 48,57 34,57 34,40 21,40 21,57 7,57 7,26 0,26" fill="var(--accent)"/>
    <rect x="39" y="4" width="7" height="12" fill="var(--accent)"/>
  </svg>
  <p class="contact-text" style="left:703px">portfolio.example/omarlowe</p>

  <!-- Education -->
  <h2 class="section-title" style="left:442px;top:300px">EDUCATION</h2>
  <div class="entry" style="left:276px;top:366px">
    <strong>Coastal Palm State College</strong><br>Harbor Point, Florida<br>September 2006 – June 2008<br>Drafting and Design A.A.
  </div>
  <div class="entry" style="left:671px;top:366px;width:240px">
    <strong>Tidewater College of Art and Design</strong><br>Riverton, Georgia<br>September 2008 – March 2014<br>Industrial Design B.F.A.
  </div>

  <!-- Work -->
  <h2 class="section-title" style="left:439px;top:473px">WORK AND EXPERIENCE</h2>
  <div class="entry" style="left:396px;top:513px">
    <strong>Riverton Furniture Outlet</strong><br>Sales Team Manager<br>August 2010 to June 2011
  </div>
  <div class="entry" style="left:724px;top:516px">
    <strong>Internship</strong><br>Designer<br>June 2013
  </div>
  <div class="entry" style="left:232px;top:584px">
    <strong>Lumen Entertainment Inc.</strong><br>Assistant Manager<br>August 2004 to January 2010
  </div>
  <div class="entry" style="left:560px;top:584px">
    <strong>Wayfare Traders</strong><br>Sales Associate<br>March 2011 to August 2011
  </div>

  <!-- Software -->
  <h2 class="section-title" style="left:291px;top:675px">SOFTWARE</h2>
  <h2 class="section-title" style="left:631px;top:675px">SKILLS</h2>

  <div class="meter" style="left:271px;top:708px"><svg viewBox="0 0 80 80"><circle class="meter-track" cx="40" cy="40" r="35" pathLength="100" stroke-dasharray="100 100" transform="rotate(-90 40 40)"/></svg><span class="meter-value">100%</span><span class="meter-label">PixelEdit</span></div>
  <div class="meter" style="left:358px;top:708px"><svg viewBox="0 0 80 80"><circle class="meter-track" cx="40" cy="40" r="35" pathLength="100" stroke-dasharray="50 100" transform="rotate(-90 40 40)"/></svg><span class="meter-value">50%</span><span class="meter-label">VectorPro</span></div>
  <div class="meter" style="left:445px;top:708px"><svg viewBox="0 0 80 80"><circle class="meter-track" cx="40" cy="40" r="35" pathLength="100" stroke-dasharray="90 100" transform="rotate(-90 40 40)"/></svg><span class="meter-value">90%</span><span class="meter-label">Shop Skills</span></div>
  <div class="meter" style="left:532px;top:708px"><svg viewBox="0 0 80 80"><circle class="meter-track" cx="40" cy="40" r="35" pathLength="100" stroke-dasharray="80 100" transform="rotate(-90 40 40)"/></svg><span class="meter-value">80%</span><span class="meter-label">Surface 3D</span></div>
  <div class="meter" style="left:271px;top:819px"><svg viewBox="0 0 80 80"><circle class="meter-track" cx="40" cy="40" r="35" pathLength="100" stroke-dasharray="70 100" transform="rotate(-90 40 40)"/></svg><span class="meter-value">70%</span><span class="meter-label">PageSet</span></div>
  <div class="meter" style="left:357px;top:819px"><svg viewBox="0 0 80 80"><circle class="meter-track" cx="40" cy="40" r="35" pathLength="100" stroke-dasharray="90 100" transform="rotate(-90 40 40)"/></svg><span class="meter-value">90%</span><span class="meter-label">RenderLight</span></div>
  <div class="meter" style="left:445px;top:819px"><svg viewBox="0 0 80 80"><circle class="meter-track" cx="40" cy="40" r="35" pathLength="100" stroke-dasharray="80 100" transform="rotate(-90 40 40)"/></svg><span class="meter-value">80%</span><span class="meter-label">SolidForge</span></div>

  <!-- Skills -->
  <div class="meter" style="left:651px;top:708px"><svg viewBox="0 0 80 80"><circle class="meter-track" cx="40" cy="40" r="35" pathLength="100" stroke-dasharray="100 100" transform="rotate(-90 40 40)"/></svg><span class="meter-value">100%</span><span class="meter-label">Creativity</span></div>
  <div class="meter" style="left:741px;top:708px"><svg viewBox="0 0 80 80"><circle class="meter-track" cx="40" cy="40" r="35" pathLength="100" stroke-dasharray="80 100" transform="rotate(-90 40 40)"/></svg><span class="meter-value">80%</span><span class="meter-label">Professionalism</span></div>
  <div class="meter" style="left:831px;top:708px"><svg viewBox="0 0 80 80"><circle class="meter-track" cx="40" cy="40" r="35" pathLength="100" stroke-dasharray="100 100" transform="rotate(-90 40 40)"/></svg><span class="meter-value">100%</span><span class="meter-label">Teamwork</span></div>
  <div class="meter" style="left:699px;top:819px"><svg viewBox="0 0 80 80"><circle class="meter-track" cx="40" cy="40" r="35" pathLength="100" stroke-dasharray="80 100" transform="rotate(-90 40 40)"/></svg><span class="meter-value">80%</span><span class="meter-label">Communication</span></div>
  <div class="meter" style="left:787px;top:819px"><svg viewBox="0 0 80 80"><circle class="meter-track" cx="40" cy="40" r="35" pathLength="100" stroke-dasharray="100 100" transform="rotate(-90 40 40)"/></svg><span class="meter-value">100%</span><span class="meter-label">Organization</span></div>
</div>
</body>
</html>
```